a mobile app for beauty salon professional to publish their service and customers to book service

I plan to create an iPhone app (support iPhone 6 and above) that will allow beauty salon professionals (e.g. hair stylist) to publish their service/business with address/geolocation and available time slots, manage their professional profile with photos, and service charges, allow the customers to search services based on locations, and book the service. customer can provide feedback/ratings on the professional's service. a reference website : http://velmo.trimbook.example/booking/

Target Market(s)

beauty and hair salon professionals and customers

Industry/Entity Type

Hair And Beauty

Font styles to use
Sans Serif
Script

Colors

Designer to choose colors to be used in the design.

Requirements
Must have
• === customer features
• - user/customer registration
• - customer browse nearby service using a map view
• - customer browse nearby service using a list view ordered by distance (e.g. km)
• - customer search salon service based on service category, price range, and profressional's rating
• - customer select a service with zoom in details : salon name, service offered, location/address, and a "booking" button
• - customer place booking by specifying service (e.g. simple cut, blow-dry, etc) required, time slot, preferred professional
• - customer payments (paypal/credit card)
• - customer can feedback/rate on the salon professional
• === salon professional features
• - user/professional registration
• - maintain professional profile (private/public), option to upload photos
• - a registered professional can register/maintain shop/business who by default is the owner of the shop/business
• - a shop owner can assign professionals to the shop/business (multiple professional can work in the same location/shop)
• - professional maintain their service and schedule (breaks, holidays, working hours, appointments, service rates)

```html
<!DOCTYPE html>
<html lang="en">
<head>
<meta charset="utf-8">
<title>Sign up</title>
<link rel="stylesheet" href="https://fonts.googleapis.com/css2?family=Open+Sans:wght@400;600;800&family=Playfair+Display:wght@900&display=swap">
<style>
  :root {
    --sky: #00ccff;
    --sky-light: #4fdcff;
    --ink: #0a0a0a;
    --paper: #ffffff;
    --photo-tone: #8a6fb8;
  }
  * { box-sizing: border-box; margin: 0; padding: 0; }
  html, body { width: 778px; height: 1200px; overflow: hidden; background: var(--paper); }
  body { font-family: "Open Sans", sans-serif; color: var(--ink); position: relative; }

  .hero { position: absolute; left: 0; top: 0; width: 778px; height: 530px; }

  .status-bar {
    position: absolute; left: 0; top: 0; width: 778px; height: 44px;
    display: flex; align-items: center; justify-content: space-between;
    padding: 0 16px; font-size: 22px; color: var(--ink);
  }
  .status-bar .carrier { display: flex; align-items: center; gap: 6px; }
  .status-bar .time { position: absolute; left: 0; right: 0; text-align: center; pointer-events: none; }
  .status-bar .battery { display: flex; align-items: center; gap: 8px; }

  .brand {
    position: absolute; top: 58px; left: 0; width: 778px; text-align: center;
    font-family: "Playfair Display", serif; font-weight: 900; font-size: 56px;
    color: var(--paper); letter-spacing: 2px;
  }

  .account-prompt {
    position: absolute; top: 560px; left: 0; width: 778px; text-align: center;
    font-size: 29px;
  }
  .account-prompt a { color: var(--sky); font-weight: 600; text-decoration: underline; }

  .role-toggle {
    position: absolute; top: 632px; left: 114px; width: 552px; height: 82px;
    display: flex; gap: 6px;
  }
  .role-toggle .role {
    flex: 1; display: flex; align-items: center; justify-content: center;
    font-family: "Playfair Display", serif; font-weight: 900; font-size: 40px;
    border: 4px solid var(--ink);
  }
  .role-toggle .role.is-active { background: var(--ink); color: var(--paper); border-radius: 41px 0 0 41px; }
  .role-toggle .role.is-idle { background: var(--paper); border-radius: 0 41px 41px 0; }

  .field {
    position: absolute; left: 114px; width: 552px; height: 82px;
    border: 2px solid var(--ink); border-radius: 41px;
    display: flex; align-items: center; justify-content: center;
    font-size: 36px;
  }
  .field-email { top: 748px; }
  .field-password { top: 868px; }
  .field .reveal { position: absolute; right: 30px; top: 22px; }

  .remember {
    position: absolute; top: 970px; left: 134px;
    display: flex; align-items: center; gap: 14px; font-size: 25px;
  }

  .submit {
    position: absolute; top: 1014px; left: 114px; width: 552px; height: 84px;
    border-radius: 42px; background: var(--sky); color: var(--paper);
    display: flex; align-items: center; justify-content: center;
    font-weight: 800; font-size: 38px; letter-spacing: 1px;
    box-shadow: 0 6px 8px rgba(0,0,0,0.18);
  }
</style>
</head>
<body>
  <svg class="hero" viewBox="0 0 778 530">
    <defs>
      <linearGradient id="hero-sky" x1="0" y1="0" x2="0" y2="1">
        <stop offset="0" stop-color="#00ccff"/>
        <stop offset="1" stop-color="#4fdcff"/>
      </linearGradient>
      <clipPath id="hero-shape">
        <polygon points="0,0 778,0 778,455 630,526 148,526 0,455"/>
      </clipPath>
    </defs>
    <polygon points="0,0 778,0 778,455 630,526 148,526 0,455" fill="url(#hero-sky)"/>
    <rect x="200" y="160" width="382" height="366" fill="var(--photo-tone)" clip-path="url(#hero-shape)"
          role="img" aria-label="Portrait photo of a client with a short haircut, seen from the side"/>
  </svg>

  <header class="status-bar">
    <span class="carrier">●●●○○ NOVA
      <svg width="24" height="18" viewBox="0 0 24 18"><path d="M2 6a14 14 0 0 1 20 0M5.5 9.5a9 9 0 0 1 13 0M9 13a4 4 0 0 1 6 0" fill="none" stroke="currentColor" stroke-width="2.4" stroke-linecap="round"/><circle cx="12" cy="16" r="1.6" fill="currentColor"/></svg>
    </span>
    <span class="time">4:21 PM</span>
    <span class="battery">
      <svg width="14" height="22" viewBox="0 0 14 22"><path d="M2 6l10 10-5 5V1l5 5L2 16" fill="none" stroke="#3a6a80" stroke-width="1.6"/></svg>
      100%
      <svg width="46" height="20" viewBox="0 0 46 20"><rect x="1" y="2" width="40" height="16" rx="3" fill="none" stroke="currentColor" stroke-width="2"/><rect x="3" y="4" width="36" height="12" rx="1.5" fill="currentColor"/><rect x="42" y="7" width="3" height="6" rx="1" fill="currentColor"/></svg>
    </span>
  </header>

  <div class="brand">KORA</div>

  <p class="account-prompt">you have an account <a href="#">sign in</a></p>

  <div class="role-toggle">
    <div class="role is-active">Business</div>
    <div class="role is-idle">Customer</div>
  </div>

  <div class="field field-email">your email</div>
  <div class="field field-password">password
    <svg class="reveal" width="54" height="38" viewBox="0 0 54 38">
      <path d="M3 19C12 7 42 7 51 19C42 31 12 31 3 19Z" fill="none" stroke="var(--ink)" stroke-width="2"/>
      <circle cx="27" cy="19" r="7" fill="none" stroke="var(--ink)" stroke-width="2"/>
      <line x1="12" y1="35" x2="44" y2="3" stroke="var(--ink)" stroke-width="2"/>
    </svg>
  </div>

  <label class="remember">
    <svg width="32" height="32" viewBox="0 0 32 32"><rect x="1.5" y="1.5" width="29" height="29" rx="4" fill="none" stroke="var(--ink)" stroke-width="2"/><circle cx="16" cy="16" r="8" fill="var(--sky)"/></svg>
    Remember me
  </label>

  <div class="submit">SIGN UP</div>
</body>
</html>
```